Korbin Ventilation's. "We're Dalton beyond the pack"!

Good day< Does your company do face mask? that is question 1. and lets finish the stationary design and I will pay for that now? 2 If your company has BLACK HATS now I would want to do some of those? 3 I notice do you do BANNER'S and or something I can put on van's magnet type or on a building! )k that's enough but for now lets start with the stationary stuff? let me know you should have my information, and the design look's GREAT!!! Thank you..

```html
<!DOCTYPE html>
<html lang="en">
<head>
<meta charset="utf-8">
<title>Korbin Ventilation's – Letterhead</title>
<link rel="stylesheet" href="https://fonts.googleapis.com/css2?family=Montserrat:wght@400;500;700;800&family=Encode+Sans+Condensed:wght@400&display=swap">
<style>
  :root {
    --backdrop: #d6d6d6;
    --paper: #ffffff;
    --ink: #1d1d1d;
    --text: #5b5b5b;
    --heading: #555555;
    --accent: #c5d86d;
    --signature-fill: #ececec;
  }
  * { box-sizing: border-box; margin: 0; padding: 0; }
  html, body {
    width: 1056px; height: 1200px; overflow: hidden;
    background: var(--backdrop);
  }
  .letterhead {
    position: absolute; left: 123px; top: 27px;
    width: 810px; height: 1146px;
    background: var(--paper);
    box-shadow: 0 10px 30px rgba(0,0,0,0.22);
    overflow: hidden;
    color: var(--text);
    font-family: "Montserrat", sans-serif;
  }

  /* Brand block */
  .brand {
    position: absolute; left: 76px; top: 62px; width: 200px;
    display: flex; flex-direction: column; align-items: center;
    color: var(--ink); font-family: "Montserrat", sans-serif; font-weight: 800;
    text-align: center;
  }
  .brand-dot { width: 68px; height: 68px; border-radius: 50%; background: var(--ink); margin-bottom: 10px; }
  .brand-name { font-size: 21px; line-height: 1.1; text-transform: uppercase; letter-spacing: 0.5px; }
  .brand-tagline { font-size: 12.5px; line-height: 1.2; margin-top: 6px; }

  /* Contact block */
  .contact {
    position: absolute; left: 569px; top: 86px;
    font-size: 13.5px; line-height: 18px; color: var(--text);
  }
  .contact-address { margin-bottom: 8px; }
  .contact-row { display: flex; align-items: center; height: 20px; }
  .contact-row svg { width: 13px; height: 13px; margin-right: 14px; flex: none; }

  /* Recipient */
  .recipient { position: absolute; left: 76px; top: 328px; }
  .letter-date { font-size: 17px; line-height: 22px; }
  .recipient-name { font-size: 27px; font-weight: 700; color: var(--heading); line-height: 34px; margin-top: 8px; }
  .recipient-title { font-size: 17px; line-height: 22px; margin-top: 4px; }

  /* Body */
  .letter-body {
    position: absolute; left: 76px; top: 470px; width: 657px;
    font-family: "Encode Sans Condensed", sans-serif;
    font-size: 15px; line-height: 28px; color: var(--text);
  }
  .letter-body p { text-align: justify; margin-bottom: 28px; }

  .sign-off {
    position: absolute; left: 76px; top: 900px;
    font-family: "Encode Sans Condensed", sans-serif; font-size: 17px; color: var(--text);
  }
  .signature {
    position: absolute; left: 76px; top: 950px; width: 86px; height: 50px;
    background: var(--signature-fill); border-radius: 4px;
  }

  .footer-bands { position: absolute; left: 0; bottom: 0; width: 810px; height: 36px; }
</style>
</head>
<body>
  <main class="letterhead">
    <header>
      <div class="brand">
        <span class="brand-dot"></span>
        <span class="brand-name">Korbin<br>Ventilation's</span>
        <span class="brand-tagline">"We're Dalton beyond the pack"</span>
      </div>

      <address class="contact" style="font-style: normal;">
        <div class="contact-address">1234 First Line Address<br>5678 Second Line Address</div>
        <div class="contact-row">
          <svg viewBox="0 0 24 24" aria-hidden="true"><path fill="#1d1d1d" d="M6.6 10.8a15.1 15.1 0 0 0 6.6 6.6l2.2-2.2c.3-.3.7-.4 1-.2 1.1.4 2.3.6 3.6.6.6 0 1 .4 1 1V20c0 .6-.4 1-1 1A17 17 0 0 1 3 4c0-.6.4-1 1-1h3.5c.6 0 1 .4 1 1 0 1.3.2 2.5.6 3.6.1.3 0 .7-.2 1z"/></svg>
          <span>(777) 888-7777</span>
        </div>
        <div class="contact-row">
          <svg viewBox="0 0 24 24" aria-hidden="true"><rect x="2" y="5" width="20" height="14" fill="#1d1d1d"/><path d="M2 5l10 8 10-8" fill="none" stroke="#fff" stroke-width="1.6"/></svg>
          <span>info@yourmail.com</span>
        </div>
        <div class="contact-row">
          <svg viewBox="0 0 24 24" aria-hidden="true"><g fill="none" stroke="#1d1d1d" stroke-width="1.6"><circle cx="12" cy="12" r="9.5"/><ellipse cx="12" cy="12" rx="4.5" ry="9.5"/><path d="M2.5 12h19M4 7h16M4 17h16"/></g></svg>
          <span>www.yourwebsite.com</span>
        </div>
      </address>
    </header>

    <section class="recipient">
      <p class="letter-date">10 December, 2020</p>
      <h1 class="recipient-name">MICHAEL SMITH</h1>
      <p class="recipient-title">Cheif Executive Officer</p>
    </section>

    <article class="letter-body">
      <p>Contrary to popular belief, Lorem Ipsum is not simply random text. It has roots in a piece of classical Latin literature from 45 BC, making it over 2000 years old. Harold Penwick, a Latin professor at Ashgrove College in Vermont, looked up one of the more obscure Latin words, consectetur.</p>
      <p>Lorem Ipsum comes from sections 1.10.32 and 1.10.33 of "de Finibus Bonorum et Malorum" (The Extremes of Good and Evil) by Varenius, written in 45 BC. This book is a treatise on the theory of ethics, very popular during the Renaissance. The first line of Lorem Ipsum.</p>
      <p>The standard chunk of Lorem Ipsum used since the 1500s is reproduced below for those interested. Sections 1.10.32 and 1.10.33 from "de Finibus Bonorum et Malorum" by Varenius are also reproduced in their exact original.</p>
      <p>The standard chunk of Lorem Ipsum used since the 1500s is reproduced below for those interested.</p>
    </article>

    <p class="sign-off">Best Regards</p>
    <div class="signature" role="img" aria-label="Handwritten signature of Michael Smith"></div>

    <svg class="footer-bands" viewBox="0 0 810 36" aria-hidden="true">
      <polygon points="0,12 622,12 616,18 0,18" fill="var(--accent)"/>
      <polygon points="0,25 613,25 636,6 810,6 810,36 0,36" fill="var(--ink)"/>
    </svg>
  </main>
</body>
</html>
```